Business Card Design Project for Harrowgate Dwellings

We need a business card design for Harrowgate Dwellings Ltd, a respected building company that specialises in high quality designer homes.

We're after a sleek, clean, modern business card (could even have an interesting shape or something different from normal business cards) with wow factor that people will remember. It also needs to look sharp and great on print.

Please see example attached (do not copy, for inspiration only).

It needs to be in line with the new logo (see attached) and look consistent with that.

The new business card should include the Certified Framers logo (see attached) as well as the company logo and the two need to look balanced and sleek in regards to their position on the card.
_______________________________________________________
Details to be included:
Dean Whitcombe
Director

M: 027 418 5302
E: dean@harrowgatedwell.co.nz
W: www.harrowgatedwell.co.nz

If you present an option for an open card, here's some additional wording we would like you to use:

Harrowgate Dwellings are a highly skilled team who specialises in residential projects, from simple homes through to top end architectural designs.
We will treat your project with integrity, the attention it deserves, and we guarantee 100% satisfaction.

Timeless craftsmanship. Uncompromising standards.

___________________________________________________________
Additional info on Harrowgate Dwellings for your consideration:

The core values of the company are integrity, trust, expertise and uncompromising standards.

Harrowgate Dwellings have been building homes for over 20 years. Only residential, from simple 2-3 bedroom homes through to top end architectural designs. They are a registered Certified Framer (the Certified Framers Guild is a highly trusted and respected organisation in New Zealand).

The team at Harrowgate Dwellings pride themselves in delivering impeccable service to their clients and position themselves as their trusted partners and friends in the construction of their most valuable asset.

Thanks! We look forward to your designs!!!

Target Market(s)

People 30 yrs+ who have an interest in owning quality homes and are prepared to pay for it. Homes built to standards, future-proofed, building savvy.

Industry/Entity Type

Construction

Requirements
Must have
• We're looking for some wow factor as well and something that stands out and people will remember

The final design should communicate timeless craftsmanship, trust, special, VALUE, exquisite, stylish, standing the test of time, no cutting corners, reliability and high standards.

The final design also needs to be sharp and look great on print. The file supplied needs to be high resolution.

```html
<!DOCTYPE html>
<html lang="en">
<head>
<meta charset="utf-8">
<title>Harrowgate Dwellings Ltd — Business Card</title>
<link rel="stylesheet" href="https://fonts.googleapis.com/css2?family=Dosis:wght@500;600;700&display=swap">
<style>
  :root {
    --bg: #1c1c1c;
    --card-black: #0b0b0b;
    --card-black-2: #1a1a1a;
    --card-white: #ffffff;
    --ink: #111111;
    --ink-soft: #2a2a2a;
    --accent: #e0241b;
    --white: #ffffff;
    --badge: #9a9a9a;
  }
  * { box-sizing: border-box; margin: 0; padding: 0; }
  html, body {
    width: 1200px; height: 900px; overflow: hidden;
    background: var(--bg);
  }
  .canvas {
    position: relative; width: 1200px; height: 900px;
    display: flex; justify-content: center; align-items: center; gap: 80px;
  }
  .card {
    position: relative; width: 340px; height: 560px;
    clip-path: polygon(34px 0, calc(100% - 34px) 0, 100% 34px, 100% calc(100% - 34px),
                       calc(100% - 34px) 100%, 34px 100%, 0 calc(100% - 34px), 0 34px);
    display: flex; flex-direction: column; align-items: center;
    font-family: "Dosis", sans-serif; text-transform: uppercase;
  }

  /* Company name lockup */
  .brand { display: flex; align-items: center; gap: 12px; justify-content: center; }
  .brand__square { width: 34px; height: 34px; background: var(--accent); flex: none; }
  .brand__name {
    font-family: "Dosis", sans-serif; font-weight: 600; font-size: 19px;
    line-height: 1.1; letter-spacing: 1px; text-align: left;
  }

  /* Front */
  .card--front {
    background: linear-gradient(160deg, var(--card-black-2), var(--card-black) 60%);
    color: var(--white);
  }
  .front-decoration {
    width: 100%; height: 280px;
    background: linear-gradient(170deg, #1e1a18 0%, #0b0b0b 60%, #121212 100%);
  }
  .front-brand { margin-top: 60px; }
  .card--front .brand__name { color: var(--white); }
  .front-web { margin-top: 30px; font-size: 14px; letter-spacing: 1px; font-weight: 600; }

  /* Back */
  .card--back { background: var(--card-white); color: var(--ink); padding-top: 92px; }
  .card--back .brand__name { color: var(--ink); }
  .contact-name { margin-top: 46px; font-size: 20px; font-weight: 600; letter-spacing: 1.5px; }
  .contact-role { font-size: 12px; font-weight: 600; letter-spacing: 1px; }
  .contact-list {
    list-style: none; margin-top: 22px; font-size: 15px; font-weight: 600;
    letter-spacing: 1px; line-height: 1.2; text-align: left;
  }
  .contact-list li:first-child { text-align: center; margin-bottom: 4px; }
  .about {
    margin-top: 26px; padding: 0 36px; font-size: 10px; font-weight: 600;
    line-height: 1.15; color: var(--ink-soft); letter-spacing: 0.3px;
  }
  .about p + p { margin-top: 7px; }
  .member-badge {
    margin-top: 24px; width: 26px; height: 30px; background: var(--badge);
  }
</style>
</head>
<body>
  <main class="canvas">
    <section class="card card--front" aria-label="Card front">
      <div class="front-decoration" role="img" aria-label="Large dark house roof and window decoration"></div>
      <div class="brand front-brand">
        <span class="brand__square"></span>
        <span class="brand__name">Harrowgate<br>Dwellings Ltd</span>
      </div>
      <div class="front-web">www.harrowgatedwell.co.nz</div>
    </section>

    <section class="card card--back" aria-label="Card back">
      <div class="brand">
        <span class="brand__square"></span>
        <span class="brand__name">Harrowgate<br>Dwellings Ltd</span>
      </div>
      <h1 class="contact-name">Dean Whitcombe</h1>
      <div class="contact-role">Director</div>
      <ul class="contact-list">
        <li>027 418 5302</li>
        <li>dean@harrowgatedwell.co.nz</li>
        <li>www.harrowgatedwell.co.nz</li>
      </ul>
      <div class="about">
        <p>Our highly skilled team specialise in residential projects, from simple homes through to top end architectural designs.</p>
        <p>We will treat your project with integrity and we guarantee 100% satisfaction.</p>
      </div>
      <div class="member-badge" role="img" aria-label="Guild membership badge"></div>
    </section>
  </main>
</body>
</html>
```